Tobin's Jewelry Studio Needs a Moving Location Flyer

We need a flyer to inform our customers of our location moving. We will be moving to our city's downtown which is only 1 mile away from our current address. We will be having a moving sale ( Up to 80% off). The sale starts Sept. 8th Our business creates, sells, and repairs fine jewelry. Dimensions are 5"x8"

Target Market(s)

Women ages 25-55

Industry/Entity Type

Jewelry

Colors
85abd2
cfdeed

Requirements
Must have
• Our logo
• Mention of the sale
• Our current address
• 4187 Marsh Creek Blvd.
• Brookhollow, Ca 91642
• (909)417-2863
Nice to have
• Mention that we're relocating to downtown Brookhollow (new location opening Nov. 1st.)

```html
<!DOCTYPE html>
<html lang="en">
<head>
<meta charset="utf-8">
<title>Tobin's Jewelry Studio – We're Relocating</title>
<link rel="stylesheet" href="https://fonts.googleapis.com/css2?family=Arimo:wght@400;700&family=Roboto+Condensed:wght@700&display=swap">
<style>
  :root {
    --sky: #85abd2;
    --sky-deep: #6b9bd0;
    --sky-light: #cfdeed;
    --glass-glow: #7fc6f0;
    --white: #ffffff;
    --navy: #1e3a8a;
    --royal: #1760b4;
    --ink: #111111;
    --rule: #e6eef8;
  }
  * { margin: 0; padding: 0; box-sizing: border-box; }
  html, body { width: 1200px; height: 751px; overflow: hidden; }
  body { background: var(--sky); font-family: "Arimo", Arial, sans-serif; }

  .flyer {
    position: relative;
    width: 1200px;
    height: 751px;
    overflow: hidden;
    background: linear-gradient(180deg, #78a9dc 0%, var(--sky-deep) 55%, #6e9fd2 100%);
  }

  /* hourglass artwork area */
  .hourglass-art {
    position: absolute;
    left: 40px;
    top: -20px;
    width: 490px;
    height: 800px;
    background:
      radial-gradient(ellipse 38% 20% at 50% 52%, rgba(140,215,250,0.85) 0%, rgba(140,215,250,0) 100%),
      radial-gradient(ellipse 48% 30% at 50% 22%, rgba(120,195,240,0.7) 0%, rgba(120,195,240,0) 100%),
      radial-gradient(ellipse 48% 30% at 50% 85%, rgba(120,195,240,0.6) 0%, rgba(120,195,240,0) 100%);
  }

  .relocating {
    position: absolute;
    left: 110px;
    top: 138px;
    width: 360px;
    text-align: center;
    font-family: "Roboto Condensed", "Arial Narrow", sans-serif;
    font-weight: 700;
    color: var(--royal);
    text-transform: uppercase;
    line-height: 1;
  }
  .relocating .line-1 { display: block; font-size: 40px; transform: rotate(4deg); }
  .relocating .line-2 { display: block; font-size: 40px; margin-top: 8px; transform: rotate(8deg); }
  .relocating .line-3 { display: block; font-size: 38px; margin-top: 8px; letter-spacing: 1px; transform: rotate(-6deg); font-family: "Arimo", Arial, sans-serif; font-weight: 400; }

  .opening {
    position: absolute;
    left: 100px;
    top: 496px;
    width: 364px;
    text-align: center;
    font-weight: 700;
    font-size: 36px;
    line-height: 45px;
    color: var(--royal);
  }

  .sale-info {
    position: absolute;
    left: 505px;
    top: 186px;
    width: 630px;
    text-align: center;
  }
  .sale-lead {
    font-weight: 700;
    font-size: 36px;
    line-height: 48px;
    color: var(--white);
  }
  .sale-lead small { font-size: 30px; }
  .sale-date {
    font-weight: 700;
    font-size: 37px;
    line-height: 48px;
    margin-top: 4px;
    color: var(--navy);
  }
  .rule {
    width: 430px;
    height: 1px;
    margin: 0 auto;
    background: var(--rule);
  }
  .rule.top { margin-top: 20px; }
  .services {
    font-weight: 700;
    font-size: 22px;
    line-height: 31px;
    color: var(--navy);
    padding: 12px 0 14px;
  }

  .brand {
    position: absolute;
    left: 600px;
    top: 530px;
    width: 430px;
    display: flex;
    align-items: center;
    justify-content: center;
    gap: 16px;
  }
  .brand-dot {
    width: 58px;
    height: 58px;
    border-radius: 50%;
    background: var(--sky-light);
  }
  .brand-name {
    font-weight: 700;
    font-size: 26px;
    color: var(--ink);
  }

  .contact {
    position: absolute;
    left: 560px;
    top: 626px;
    width: 520px;
    text-align: center;
    font-size: 22px;
    line-height: 38px;
    color: var(--ink);
  }
  .phone { display: inline-flex; align-items: center; gap: 10px; }
  .phone svg { width: 28px; height: 28px; }
</style>
</head>
<body>
<main class="flyer">
  <div class="hourglass-art" role="img" aria-label="Glowing glass hourglass illustration in light blue tones"></div>

  <h1 class="relocating">
    <span class="line-1">We're relocating</span>
    <span class="line-2">to downtown</span>
    <span class="line-3">Brookhollow</span>
  </h1>

  <p class="opening">NEW<br>LOCATION<br>OPENING<br>NOVEMBER 1ST</p>

  <section class="sale-info">
    <p class="sale-lead">We will be having a<br>moving sale (<small>Up to</small> 80% off)</p>
    <p class="sale-date">The sale starts September 8th</p>
    <div class="rule top"></div>
    <p class="services">Our business creates, sells, and<br>repairs fine jewelry</p>
    <div class="rule"></div>
  </section>

  <div class="brand">
    <span class="brand-dot"></span>
    <span class="brand-name">Tobin's Jewelry Studio</span>
  </div>

  <address class="contact" style="font-style:normal">
    <div>4187 Marsh Creek Blvd., Brookhollow, Ca 91642</div>
    <div class="phone">
      <svg viewBox="0 0 28 28" aria-hidden="true">
        <circle cx="14" cy="14" r="12.5" fill="none" stroke="#111" stroke-width="1.6"/>
        <path d="M10 7.5c-1.2.6-2.4 2-2 4 .8 3.6 4.8 8 8.4 9 2 .5 3.4-.6 4-1.8l-2.6-2.4-1.8 1.2c-1.8-.8-3.8-3-4.6-4.8l1.2-1.8z" fill="#111"/>
      </svg>
      <span>(909)417-2863</span>
    </div>
  </address>
</main>
</body>
</html>
```